Portada libro no ficción: Rutas de comercio hacia la Nubeterra

Busco diseño para libro de no ficción sobre los modelos de negocio del metaverso.

Maquetación de:
- Portada
- Contraportada
- Lomo

Requerimientos:
- Una portada única y creativa
- Portada para formato Lectar, Vendaro y físico.
- Imágenes para el sitio web y las redes sociales
- Gráficos profesionales de alta calidad
- Adjuntar archivo de edición

Target:
- CEO
- CMO
- Emprendedor
- Gente relacionada con el marketing digital

Ideas iniciales de la portada:
- Minimalista
- Atemporal: Evitar gafas de realidad virtual (son productos que cambian con frecuencia)

Descripción del libro:
No se trata de un libro técnico sobre el metaverso. El objetivo del libro es llegar a marketers, CEOs, emprendedores, perfiles tecnológicos con visión de negocio que quieren descubrir cómo llevar su negocio o su idea de negocio al metaverso, y cómo aplicar modelos de negocio.

El libro se divide en un primer bloque de presentación del metaverso, introducción a la economía digital, y modelos de negocio aplicados al metaverso.

Ejemplos de portada:
- cover1: este formato es mi favorito, minimalista, atemporal y fácil de leer.
- cover2: esta portada me parece interesante por la cercanía con los colores habituales del metaverso.
- cover3: aunque con un toque retro (no es lo que busco), es un formato que me parece interesante por no recurrir a las gafas, y sin entrar en formato fotografía.
- cover4 y cover5: me gusta la relación de colores entre la letra y el fondo para dar prioridad al título.
- cover6: me gusta usar dos colores, en este caso para destacar metaverso, y la imagen de la portada te hace sentir más listo (por pensar diferente).

Título: "Rutas de comercio hacia la nubeterra"

Texto asociado:
"Lidera la transición de tu negocio hacia el metaverso"

"Descubre los principales modelos de negocio del metaverso y cómo aplicarlos"

Autor: Tomàs Valbuena

```html
<!DOCTYPE html>
<html lang="es">
<head>
<meta charset="utf-8">
<title>Rutas de comercio hacia la Nubeterra — Portada</title>
<link rel="stylesheet" href="https://fonts.googleapis.com/css2?family=Oswald:wght@400;500&family=Roboto:wght@400&display=swap">
<style>
  :root {
    --page-bg: #ffffff;
    --ink-light: #ffffff;
    --night-deep: #07131f;
    --night-mid: #0c2b40;
    --cyan-glow: #27c3e0;
    --cyan-soft: #7fe6f5;
    --floor-dark: #050d16;
  }
  * { margin: 0; padding: 0; box-sizing: border-box; }
  html, body {
    width: 1200px;
    height: 1196px;
    overflow: hidden;
    background: var(--page-bg);
  }
  .book-cover {
    position: absolute;
    left: 276px;
    top: 113px;
    width: 648px;
    height: 970px;
    overflow: hidden;
    color: var(--ink-light);
    text-align: center;
  }
  .cover-art {
    position: absolute;
    inset: 0;
    background:
      radial-gradient(ellipse 55% 35% at 50% 68%, rgba(127, 230, 245, 0.55), rgba(39, 195, 224, 0) 70%),
      radial-gradient(ellipse 80% 45% at 50% 52%, rgba(39, 195, 224, 0.6), rgba(12, 43, 64, 0) 75%),
      linear-gradient(180deg, var(--night-deep) 0%, var(--night-mid) 22%, #136a8a 45%, #1a9cbc 60%, #0d3e57 78%, var(--floor-dark) 100%);
  }
  .tagline {
    position: absolute;
    top: 20px;
    left: 0;
    right: 0;
    font-family: "Oswald", sans-serif;
    font-weight: 500;
    font-size: 20px;
    letter-spacing: 0.6px;
  }
  .title {
    position: absolute;
    top: 100px;
    left: 0;
    right: 0;
    font-family: "Oswald", sans-serif;
    font-weight: 400;
    line-height: 1;
  }
  .title-line {
    display: block;
    font-size: 66px;
    line-height: 62px;
  }
  .title-key {
    display: block;
    font-size: 128px;
    line-height: 140px;
    letter-spacing: 1px;
  }
  .subtitle {
    position: absolute;
    top: 825px;
    left: 60px;
    right: 60px;
    font-family: "Roboto", sans-serif;
    font-size: 19px;
    line-height: 25px;
  }
  .author {
    position: absolute;
    top: 900px;
    left: 0;
    right: 0;
    font-family: "Oswald", sans-serif;
    font-weight: 400;
    font-size: 31px;
    letter-spacing: 1.5px;
  }
</style>
</head>
<body>
  <main class="book-cover">
    <div class="cover-art" role="img" aria-label="Ilustración de una ciudad futurista en tonos cian con una figura de pie en el centro de una avenida luminosa"></div>
    <p class="tagline">'LIDERA LA TRANSICIÓN DE TU NEGOCIO HACIA EL METAVERSO'</p>
    <h1 class="title">
      <span class="title-line">Rutas de comercio</span>
      <span class="title-line">hacia la</span>
      <span class="title-key">NUBETERRA</span>
    </h1>
    <p class="subtitle">"Descubre los principales modelos de negocio del metaverso y cómo aplicarlos"</p>
    <p class="author">TOMÀS VALBUENA</p>
  </main>
</body>
</html>
```